Sandwich Board and Poster design promoting a medical aesthetic clinic

I am looking for a clean, modern and relaxing design promoting a medical physician-led aesthetic clinic.
Services offered are neuromodulator treatment (Quelvo) and Dermal Fillers.
Logo must be included.
Use the tag line "Refresh your look, revive your spirit."
Address is 204-205 27361 92 Ave, Surrey, V7K 2M4
604-555-0148
email - info@lumawellpine.ca
www.lumawellpine.ca

```html
<!DOCTYPE html>
<html lang="en">
<head>
<meta charset="utf-8">
<title>Lumawell Pine – Refresh your look</title>
<link href="https://fonts.googleapis.com/css2?family=Montserrat:wght@400&family=Poppins:wght@400;700;800&display=swap" rel="stylesheet">
<style>
  :root {
    --stage: #5f6a70;
    --ink: #0b0b0b;
    --paper: #ffffff;
    --gold: #e2b928;
    --sky: #8fd3ec;
    --skin: #c9906c;
  }
  * { margin: 0; padding: 0; box-sizing: border-box; }
  html, body { width: 1200px; height: 1200px; overflow: hidden; background: var(--stage); }
  .poster {
    position: absolute; left: 261px; top: 93px;
    width: 677px; height: 1013px;
    background: var(--paper); overflow: hidden;
    font-family: "Poppins", sans-serif; color: var(--ink);
  }
  .hero-photo {
    position: absolute; left: 0; top: 0; width: 677px; height: 470px;
    background:
      radial-gradient(ellipse 380px 200px at 440px 220px, #b98563 0%, rgba(185,133,99,0) 100%),
      linear-gradient(200deg, #3fc0e6 0%, var(--sky) 30%, #e8eef2 55%, #d7b39a 75%, var(--skin) 100%);
  }
  .arch { position: absolute; left: 0; top: 0; width: 677px; height: 1013px; }
  .brand {
    position: absolute; left: 0; width: 100%; top: 470px; text-align: center;
    font-family: "Montserrat", sans-serif; font-weight: 400;
    font-size: 26px; letter-spacing: 8px; color: var(--ink);
  }
  .headline {
    position: absolute; left: 0; width: 100%; text-align: center;
    font-weight: 700; letter-spacing: -1px; line-height: 1;
  }
  .headline-refresh { top: 548px; font-size: 106px; }
  .headline-look { top: 648px; font-size: 106px; }
  .tagline {
    position: absolute; left: 0; width: 100%; top: 752px; text-align: center;
    font-weight: 700; font-size: 38px; line-height: 44px;
  }
  .address {
    position: absolute; left: 0; width: 100%; top: 827px;
    display: flex; justify-content: center; align-items: center; gap: 10px;
    font-size: 21px; font-weight: 400;
  }
  .address svg { width: 20px; height: 20px; }
  .phone-pill {
    position: absolute; left: 115px; top: 884px; width: 460px; height: 60px;
    background: var(--gold); border: 2px solid var(--ink); border-radius: 30px;
    display: flex; align-items: center; padding-left: 6px; gap: 12px;
  }
  .phone-pill svg { width: 48px; height: 48px; flex: none; }
  .phone-number { font-weight: 800; font-size: 44px; letter-spacing: 1px; line-height: 1; }
  .footer-band {
    position: absolute; left: 0; top: 916px; width: 677px; height: 97px;
    background: linear-gradient(90deg, #000 0%, #1d1d1d 60%, #2a2a2a 100%);
  }
  .poster .phone-pill { z-index: 2; }
  .contact-row {
    position: absolute; left: 0; width: 100%; top: 964px;
    display: flex; justify-content: center; align-items: center; gap: 22px;
    color: var(--paper); font-size: 19px;
  }
  .contact-item { display: flex; align-items: center; gap: 10px; }
  .contact-item svg { width: 20px; height: 20px; }
  .contact-divider { width: 1px; height: 26px; background: #8a8a8a; }
</style>
</head>
<body>
  <main class="poster">
    <div class="hero-photo" role="img" aria-label="Photo of a woman relaxing on a treatment bed while a gloved practitioner gives a cosmetic injection near her temple"></div>

    <svg class="arch" viewBox="0 0 677 1013" aria-hidden="true">
      <path fill="#0b0b0b" d="M0,447 C90,370 230,332 338,332 C450,332 590,375 677,453 L677,1013 L0,1013 Z"/>
      <path fill="#e2b928" d="M0,555 C50,440 200,348 338,346 C480,348 630,440 677,555 L677,1013 L0,1013 Z"/>
      <path fill="#ffffff" d="M0,590 C50,450 200,352 338,350 C480,352 630,450 677,590 L677,1013 L0,1013 Z"/>
      <polygon fill="#e2b928" points="115,748 578,748 615,801 99,801"/>
      <polygon fill="#0b0b0b" points="92,736 106,736 80,801 66,801"/>
      <polygon fill="#0b0b0b" points="562,708 578,708 644,801 628,801"/>
    </svg>

    <div class="brand">LUMAWELL PINE</div>

    <h1 class="headline headline-refresh">Refresh</h1>
    <div class="headline headline-look">your look</div>
    <p class="tagline">Revive your spirit</p>

    <p class="address">
      <svg viewBox="0 0 24 24" aria-hidden="true"><path fill="#0b0b0b" d="M12 1a9 9 0 0 0-9 9c0 6.5 9 13 9 13s9-6.5 9-13a9 9 0 0 0-9-9z"/><circle cx="12" cy="10" r="4" fill="#e2b928"/></svg>
      <span>204-205 27361 92 Ave, Surrey, V7K 2M4</span>
    </p>

    <div class="footer-band"></div>

    <div class="phone-pill">
      <svg viewBox="0 0 48 48" aria-hidden="true"><circle cx="24" cy="24" r="23" fill="#0b0b0b"/><path fill="#ffffff" d="M17 12c1-1 2.5-1 3.3.2l2.6 3.8c.7 1 .5 2.3-.4 3.1l-1.8 1.5c1.3 3 3.6 5.4 6.6 6.8l1.5-1.8c.8-.9 2.1-1.1 3.1-.4l3.8 2.6c1.2.8 1.3 2.4.3 3.4l-2 2c-1.6 1.6-4 2.1-6.1 1.2-6.3-2.7-11-7.5-13.6-13.8-.9-2.1-.3-4.5 1.3-6.1z"/></svg>
      <span class="phone-number">604-555-0148</span>
    </div>

    <div class="contact-row">
      <span class="contact-item">
        <svg viewBox="0 0 24 24" aria-hidden="true"><rect x="2" y="5" width="20" height="14" rx="1" fill="#e2b928"/><path d="M2 6l10 7 10-7" fill="none" stroke="#111" stroke-width="1.6"/></svg>
        info@lumawellpine.ca
      </span>
      <span class="contact-divider"></span>
      <span class="contact-item">
        <svg viewBox="0 0 24 24" aria-hidden="true"><g fill="none" stroke="#e2b928" stroke-width="1.6"><circle cx="12" cy="12" r="9.5"/><ellipse cx="12" cy="12" rx="4.5" ry="9.5"/><path d="M2.5 12h19M4 7h16M4 17h16"/></g></svg>
        www.lumawellpine.ca
      </span>
    </div>
  </main>
</body>
</html>
```